New business card design needed for Diesel Fitting (Mechanical) Company

We need a new business card for our company called "Gumtree Engine Works" that showcases our logo and business details.
Target Market(s)
Owners of all makes and models of vehicles, trucks, plant and machinery.
Industry/Entity Type
Mechanical
Contact Information for Business Card
The business card details need to include the following: Owners/Directors: Doug & Marisol Brent-Coyle ABN: 41 917 302 846 Address: 317 Wattlebrook Street KELLERBY DOWNS QLD 4862 Postal Address: PO Box 5791 KELLERBY DOWNS QLD 4862 Website: www.gewservice.com.au Phone: 4712 9083 Mobile: 0438 175 906 Emails: sales@gewservice.com.au; admin@gewservice.com.au; accounts@gewservice.com.au; parts@gewservice.com.au; office@gewservice.com.au, reception@gewservice.com.au
Look and feel

```html
<!DOCTYPE html>
<html lang="en">
<head>
<meta charset="utf-8">
<title>Gumtree Engine Works – Business Card</title>
<link rel="stylesheet" href="https://fonts.googleapis.com/css2?family=Questrial&display=swap">
<style>
  :root {
    --backdrop: #0e0e0f;
    --card: #2a2a2c;
    --card-back: #262628;
    --orange: #f26b21;
    --text: #bdbdbd;
    --rule: #5e5e60;
    --emboss: #58585b;
  }
  * { box-sizing: border-box; margin: 0; padding: 0; }
  html, body { width: 1200px; height: 820px; overflow: hidden; }
  body {
    background: radial-gradient(ellipse at center, #1c1c1d 0%, var(--backdrop) 75%);
    font-family: "Questrial", "Century Gothic", sans-serif;
    color: var(--text);
    position: relative;
  }
  .card {
    position: absolute;
    top: 240px;
    width: 560px;
    height: 340px;
    border-left: 3px solid var(--orange);
    border-bottom: 3px solid var(--orange);
    box-shadow: 0 12px 40px rgba(0,0,0,.6);
  }
  .card--front { left: 20px; background: var(--card); }
  .card--back  { left: 620px; background: var(--card-back); display: flex; align-items: center; justify-content: center; }

  .owners { position: absolute; left: 28px; top: 28px; }
  .owners__name { color: var(--orange); font-size: 19px; }
  .owners__role { font-size: 15px; margin-top: 2px; }

  .brand-name { position: absolute; right: 28px; top: 48px; color: var(--orange); font-size: 22px; }
  .brand-name--emboss { position: static; color: var(--emboss); font-size: 32px; }

  .header-rule { position: absolute; left: 250px; right: 28px; top: 96px; height: 1px; background: var(--rule); }

  .addresses { position: absolute; right: 28px; top: 108px; text-align: right; font-size: 14px; line-height: 17px; }
  .address { display: flex; justify-content: flex-end; gap: 8px; margin-bottom: 9px; }
  .address__pin { width: 11px; height: 15px; flex: none; margin-top: 1px; }

  .contacts { position: absolute; left: 28px; top: 120px; font-size: 15px; }
  .contact-line { display: flex; align-items: center; gap: 9px; height: 21px; }
  .contact-line svg { width: 14px; height: 14px; flex: none; }
  .accent { color: var(--orange); }

  .contacts-rule { position: absolute; left: 28px; width: 250px; top: 192px; height: 1px; background: var(--rule); }

  .emails { position: absolute; left: 28px; top: 201px; list-style: none; font-size: 14.5px; }
  .emails li { display: flex; align-items: center; gap: 9px; height: 21px; }
  .emails svg { width: 15px; height: 11px; flex: none; }
</style>
</head>
<body>

<section class="card card--front" aria-label="Business card front">
  <div class="owners">
    <p class="owners__name">Doug &amp; Marisol Brent-Coyle</p>
    <p class="owners__role">Owners/Directors</p>
  </div>

  <p class="brand-name">Gumtree Engine Works</p>
  <div class="header-rule"></div>

  <div class="addresses">
    <div class="address">
      <p>317 Wattlebrook Street<br>KELLERBY DOWNS<br>QLD 4862</p>
      <svg class="address__pin" viewBox="0 0 11 15"><path d="M5.5 0C2.5 0 0 2.4 0 5.4 0 9.2 5.5 15 5.5 15S11 9.2 11 5.4C11 2.4 8.5 0 5.5 0z" fill="var(--orange)"/><circle cx="5.5" cy="5.4" r="2" fill="var(--card)"/></svg>
    </div>
    <div class="address">
      <p>PO Box 5791<br>KELLERBY DOWNS<br>QLD 4862</p>
      <svg class="address__pin" viewBox="0 0 11 15"><path d="M5.5 0C2.5 0 0 2.4 0 5.4 0 9.2 5.5 15 5.5 15S11 9.2 11 5.4C11 2.4 8.5 0 5.5 0z" fill="var(--orange)"/><circle cx="5.5" cy="5.4" r="2" fill="var(--card)"/></svg>
    </div>
  </div>

  <div class="contacts">
    <p class="contact-line">
      <svg viewBox="0 0 14 14"><path d="M3 1l2 3-1.3 1.3a8 8 0 0 0 5 5L10 9l3 2-1.2 2C6.5 13 1 7.5 1 2.2z" fill="none" stroke="var(--orange)" stroke-width="1.4" stroke-linejoin="round"/></svg>
      <span>4712 9083</span>
    </p>
    <p class="contact-line">
      <svg viewBox="0 0 14 14"><rect x="3.5" y="0.8" width="7" height="12.4" rx="1.2" fill="none" stroke="var(--orange)" stroke-width="1.4"/><line x1="6" y1="11" x2="8" y2="11" stroke="var(--orange)" stroke-width="1.2"/></svg>
      <span>0438 175 906</span>
    </p>
    <p class="contact-line">
      <svg viewBox="0 0 14 14" fill="none" stroke="var(--orange)" stroke-width="1.2"><circle cx="7" cy="7" r="6"/><ellipse cx="7" cy="7" rx="2.6" ry="6"/><line x1="1" y1="7" x2="13" y2="7"/><line x1="2" y1="4" x2="12" y2="4"/><line x1="2" y1="10" x2="12" y2="10"/></svg>
      <span>www.<span class="accent">gewservice</span>.com.au</span>
    </p>
  </div>

  <div class="contacts-rule"></div>

  <ul class="emails">
    <li><svg viewBox="0 0 15 11"><rect width="15" height="11" fill="var(--orange)"/><path d="M0 0l7.5 6L15 0M0 11l5.5-5M15 11L9.5 6" fill="none" stroke="var(--card)" stroke-width="1.2"/></svg><span>sales@gewservice.com.au</span></li>
    <li><svg viewBox="0 0 15 11"><rect width="15" height="11" fill="var(--orange)"/><path d="M0 0l7.5 6L15 0M0 11l5.5-5M15 11L9.5 6" fill="none" stroke="var(--card)" stroke-width="1.2"/></svg><span>admin@gewservice.com.au</span></li>
    <li><svg viewBox="0 0 15 11"><rect width="15" height="11" fill="var(--orange)"/><path d="M0 0l7.5 6L15 0M0 11l5.5-5M15 11L9.5 6" fill="none" stroke="var(--card)" stroke-width="1.2"/></svg><span>accounts@gewservice.com.au</span></li>
    <li><svg viewBox="0 0 15 11"><rect width="15" height="11" fill="var(--orange)"/><path d="M0 0l7.5 6L15 0M0 11l5.5-5M15 11L9.5 6" fill="none" stroke="var(--card)" stroke-width="1.2"/></svg><span>parts@gewservice.com.au</span></li>
    <li><svg viewBox="0 0 15 11"><rect width="15" height="11" fill="var(--orange)"/><path d="M0 0l7.5 6L15 0M0 11l5.5-5M15 11L9.5 6" fill="none" stroke="var(--card)" stroke-width="1.2"/></svg><span>office@gewservice.com.au</span></li>
    <li><svg viewBox="0 0 15 11"><rect width="15" height="11" fill="var(--orange)"/><path d="M0 0l7.5 6L15 0M0 11l5.5-5M15 11L9.5 6" fill="none" stroke="var(--card)" stroke-width="1.2"/></svg><span>reception@gewservice.com.au</span></li>
  </ul>
</section>

<section class="card card--back" aria-label="Business card back">
  <p class="brand-name brand-name--emboss">Gumtree Engine Works</p>
</section>

</body>
</html>
```